Velmoran Tabletop Deck Company (southern african focus for now) needs a e-commerce website

We need a website design for a playing card company based in Southern Africa/United States. We make locally-sourced playing cards (standard 52 card deck, with customized fronts and backs) for everyone and collaborate with local artists to uplift their talents, while celebrating their nation's culture, heritage, beauty and identity. We would like to see designs that use the colours blue (see flag of Eswatini as starting product), white and some red accents (or your recommendation). The final design should communicate elegance, fun and sustainable prosperity.

Target Market(s)

Everyone loves playing cards. From the solo adventurer to the party host, first time learner or expert, young, middle and old, we need to attract a broad audience that appreciates the finer things and supports sustainable, environmentally contentiousness causes that support the local economy and uplift local talent - thing global, act local.

Number of Pages Required

4 page

Font styles to use
Serif
Sans Serif

Requirements
Must have
• Pages to include Home (Main), About (Our Story), Shop and Contact
Nice to have
• While designs may be static, elements of graceful movement would be desirable. Perhaps functionality of scrolling down on homepage showing playing cards in use, front and back. Quindle and Zorbix store's capture that elegant yet rich look.
Should not have
• Too many products. We focus on 1-2.

```html
<!DOCTYPE html>
<html lang="en">
<head>
<meta charset="utf-8">
<title>Velmoran – Contact</title>
<link href="https://fonts.googleapis.com/css2?family=Open+Sans:wght@400;600;700&display=swap" rel="stylesheet">
<style>
  :root{
    --ink:#111;
    --muted:#555;
    --panel-blue:#3f5db6;
    --field-blue:#7a8fcc;
    --accent-red:#b80f0f;
    --white:#fff;
    --bar:#333;
    --bar-text:#aaa;
    --flag-blue:#3e5eb9;
    --flag-yellow:#ffd900;
    --flag-red:#b10c0c;
  }
  *{box-sizing:border-box;margin:0;padding:0}
  html,body{width:1200px;height:1016px;overflow:hidden;background:var(--white)}
  body{position:relative;font-family:"Open Sans",sans-serif;color:var(--ink)}
  .abs{position:absolute}

  .brand{left:78px;top:19px;font-size:19px;font-weight:600;letter-spacing:.5px}
  .nav{top:22px;font-size:14px;letter-spacing:1.5px}
  .cart{left:952px;top:20px}
  .locale{left:1023px;top:21px;display:flex;align-items:center;gap:10px;font-size:11.5px;letter-spacing:1px;color:#333}
  .flag{width:31px;height:20px;display:block}

  .page-title{left:0;width:1200px;top:124px;text-align:center;font-size:31px;letter-spacing:3.5px}

  .form-panel{left:258px;top:244px;width:446px;height:318px;background:var(--panel-blue);box-shadow:0 1px 3px rgba(0,0,0,.2)}
  .label{color:var(--white);font-size:10.5px;letter-spacing:.6px}
  .field{background:var(--field-blue);border-radius:1px}
  .submit{left:379px;top:494px;width:72px;height:18px;background:var(--accent-red);color:var(--white);font-size:9px;letter-spacing:.7px;text-align:center;line-height:18px;border-radius:1px}

  .info-card{left:704px;top:234px;width:240px;height:338px;background:var(--white);box-shadow:0 0 6px rgba(0,0,0,.15)}
  .info-title{left:704px;width:240px;top:250px;text-align:center;font-size:11.5px;letter-spacing:1px;color:#222}
  .info-line{font-size:7.5px;letter-spacing:.9px;color:#222;white-space:nowrap;display:flex;align-items:center;gap:4px}

  .banner{left:0;top:704px;width:1200px;height:104px;background:linear-gradient(100deg,#e8e2dc 0%,#f2ece8 25%,#c9b9a6 45%,#ede6df 60%,#f3eeeb 80%,#e6dcd6 100%)}
  .banner-name{left:0;width:1200px;top:716px;text-align:center;font-size:50px;font-weight:600;color:#161616;letter-spacing:1px}

  .col-head{font-size:16px;letter-spacing:2px;text-align:center}
  .rule{height:1px;background:var(--panel-blue)}
  .foot-link{font-size:11.5px;letter-spacing:1.8px;text-align:center;width:120px;left:236px}
  .social{font-size:7px;letter-spacing:.4px;display:flex;align-items:center;gap:3px}
  .dot{width:9px;height:9px;border-radius:50%;background:#111;display:inline-block}
  .badge{background:#000;color:var(--white);border-radius:4px;font-size:11px;font-weight:600;display:flex;align-items:center;justify-content:center;border:1px solid #777}

  .bottom-bar{left:0;top:971px;width:1200px;height:45px;background:var(--bar)}
  .bar-text{top:988px;font-size:7.5px;letter-spacing:.8px;color:var(--bar-text);white-space:nowrap}
</style>
</head>
<body>
  <header>
    <div class="abs brand">Velmoran</div>
    <nav>
      <span class="abs nav" style="left:579px">Home</span>
      <span class="abs nav" style="left:664px">About</span>
      <span class="abs nav" style="left:750px">Shop</span>
      <span class="abs nav" style="left:830px">Contact</span>
    </nav>
    <svg class="abs cart" width="23" height="22" viewBox="0 0 24 24" aria-label="Cart"><path fill="#111" d="M7 18a2 2 0 1 0 0 4 2 2 0 0 0 0-4zm10 0a2 2 0 1 0 0 4 2 2 0 0 0 0-4zM1 2v2h2l3.6 7.6-1.4 2.4A2 2 0 0 0 7 17h12v-2H7.4l1.1-2h7.5a2 2 0 0 0 1.7-1l3.6-6.5A1 1 0 0 0 20.4 4H5.2l-.9-2H1z"/></svg>
    <div class="abs locale">
      <svg class="flag" viewBox="0 0 31 20" aria-label="Eswatini">
        <rect width="31" height="20" fill="var(--flag-blue)"/>
        <rect y="5" width="31" height="10" fill="var(--flag-yellow)"/>
        <rect y="6" width="31" height="8" fill="var(--flag-red)"/>
      </svg>
      <span>Eswatini ▾</span>
    </div>
  </header>

  <h1 class="abs page-title" style="font-weight:400">Contact</h1>

  <section>
    <div class="abs form-panel"></div>
    <span class="abs label" style="left:334px;top:295px">Name :</span>
    <div class="abs field" style="left:380px;top:295px;width:134px;height:15px"></div>
    <span class="abs label" style="left:334px;top:329px">Email :</span>
    <div class="abs field" style="left:379px;top:327px;width:136px;height:18px"></div>
    <span class="abs label" style="left:334px;top:363px">Title :</span>
    <div class="abs field" style="left:379px;top:361px;width:136px;height:18px"></div>
    <span class="abs label" style="left:334px;top:397px">Message</span>
    <div class="abs field" style="left:334px;top:424px;width:181px;height:57px"></div>
    <div class="abs submit">Submit</div>

    <div class="abs info-card"></div>
    <div class="abs info-title">Contact Info</div>
    <div class="abs info-line" style="left:722px;top:358px">
      <svg width="13" height="10" viewBox="0 0 13 10"><rect width="13" height="10" fill="#111"/><path d="M0 0l6.5 5L13 0" stroke="#fff" fill="none"/></svg>
      <span style="margin-left:3px">Email:&nbsp; hello@velmoran.example</span>
    </div>
    <div class="abs info-line" style="left:722px;top:395px">
      <svg width="12" height="12" viewBox="0 0 24 24"><path fill="#111" d="M6.6 10.8a15 15 0 0 0 6.6 6.6l2.2-2.2a1 1 0 0 1 1-.3 11 11 0 0 0 3.6.6 1 1 0 0 1 1 1V20a1 1 0 0 1-1 1A17 17 0 0 1 3 4a1 1 0 0 1 1-1h3.5a1 1 0 0 1 1 1c0 1.3.2 2.5.6 3.6a1 1 0 0 1-.3 1z"/></svg>
      <span style="margin-left:4px">International Branch:&nbsp; ○ +1 (555) 014-2290</span>
    </div>
    <div class="abs info-line" style="left:740px;top:414px">Corporate Office:&nbsp; ○ &nbsp;+268 70000418</div>
  </section>

  <div class="abs banner" role="img" aria-label="Photograph of playing cards spread on a table"></div>
  <div class="abs banner-name">Velmoran</div>

  <footer>
    <div class="abs col-head" style="left:236px;width:120px;top:831px">Links</div>
    <div class="abs rule" style="left:259px;top:856px;width:75px"></div>
    <div class="abs foot-link" style="top:869px">Home</div>
    <div class="abs foot-link" style="top:893px">About</div>
    <div class="abs foot-link" style="top:914px">Shop</div>
    <div class="abs foot-link" style="top:937px">Contact</div>

    <div class="abs col-head" style="left:541px;width:120px;top:831px">Contact</div>
    <div class="abs rule" style="left:563px;top:856px;width:75px"></div>
    <div class="abs social" style="left:558px;top:887px"><i class="dot"></i>Chirpa</div>
    <div class="abs social" style="left:606px;top:887px"><i class="dot"></i>Workvine</div>
    <div class="abs social" style="left:558px;top:911px"><i class="dot"></i>Friendloop</div>
    <div class="abs social" style="left:606px;top:911px"><i class="dot"></i>Picora</div>

    <div class="abs col-head" style="left:788px;width:200px;top:831px">Download App</div>
    <div class="abs rule" style="left:845px;top:856px;width:75px"></div>
    <div class="abs badge" style="left:844px;top:871px;width:80px;height:26px">Zorbix</div>
    <div class="abs badge" style="left:845px;top:915px;width:81px;height:25px">Quindle</div>

    <div class="abs bottom-bar"></div>
    <span class="abs bar-text" style="left:72px">Copyright © Velmoran 2020 &nbsp;&nbsp;&nbsp; All rights reserved.</span>
    <span class="abs bar-text" style="left:626px">Corporate Office: &nbsp;○ +268 70000418</span>
    <span class="abs bar-text" style="left:805px">International Branch: &nbsp;○ +1 (555) 014-2290</span>
    <span class="abs bar-text" style="left:1013px">Email: &nbsp;hello@velmoran.example</span>
  </footer>
</body>
</html>
```